Business Card Design

Recruitment Company. Want to keep the logo and the green colour

Industry/Entity Type

Business

Contact Information for Business Card

Hi,

1.)
MARTIN COLLARD
Director
Level 4, 238 Finch Terrace
Brisbane QLD 4000
M 0412 604 337
E martin@paceltalent.com.au
www.paceltalent.com.au

2.)
TOM WHITFORD
Director
Level 4, 238 Finch Terrace
Brisbane QLD 4000
M 0419 572 641
E tom@paceltalent.com.au

Want something different and eye catching, happy for you guys to use your design flare to work some magic with these.

Many Thanks
Tom

```html
<!DOCTYPE html>
<html lang="en">
<head>
<meta charset="utf-8">
<title>Pacel Talent – Business Card</title>
<link rel="stylesheet" href="https://fonts.googleapis.com/css2?family=Open+Sans:wght@400;600;700&display=swap">
<style>
  :root {
    --bg: #2a2a2a;
    --green-dark: #3f8f2a;
    --green: #5fae2e;
    --green-light: #9ccc2c;
    --lime: #b5d334;
    --paper: #ffffff;
    --paper-shade: #ececec;
    --ink: #222222;
  }
  * { margin: 0; padding: 0; box-sizing: border-box; }
  html, body {
    width: 1200px;
    height: 900px;
    overflow: hidden;
    background: var(--bg);
    font-family: "Open Sans", Arial, sans-serif;
  }
  .canvas {
    position: relative;
    width: 1200px;
    height: 900px;
  }
  .card {
    position: absolute;
    top: 170px;
    width: 370px;
    height: 560px;
    border-radius: 30px;
    overflow: hidden;
    box-shadow: 0 10px 30px rgba(0,0,0,.45);
  }
  /* Front */
  .card-front {
    left: 195px;
    background: var(--green);
  }
  .front-art {
    position: absolute;
    inset: 0;
    background:
      radial-gradient(ellipse at 30% 30%, var(--lime) 0%, rgba(181,211,52,0) 55%),
      radial-gradient(ellipse at 75% 80%, var(--green-light) 0%, rgba(156,204,44,0) 60%),
      linear-gradient(160deg, var(--green-light) 0%, var(--green) 55%, var(--green-dark) 100%);
  }
  .front-brand {
    position: absolute;
    left: 0; right: 0;
    top: 250px;
    text-align: center;
    color: var(--paper);
    font-weight: 700;
    font-size: 40px;
    letter-spacing: .5px;
  }
  /* Back */
  .card-back {
    left: 635px;
    background: linear-gradient(180deg, var(--paper) 0%, var(--paper-shade) 100%);
  }
  .back-brand {
    position: absolute;
    left: 0; right: 0;
    top: 80px;
    text-align: center;
    color: var(--green);
    font-weight: 700;
    font-size: 36px;
  }
  .contact {
    position: absolute;
    left: 44px;
    top: 270px;
    color: var(--ink);
    font-size: 16px;
    line-height: 1.35;
  }
  .contact-name {
    color: var(--green);
    font-weight: 700;
    font-size: 16px;
    letter-spacing: .3px;
  }
  .contact-role { margin-bottom: 16px; }
  .contact-line .label {
    display: inline-block;
    width: 18px;
    color: var(--green);
  }
  .contact-address { margin-top: 16px; }
  .footer-band {
    position: absolute;
    left: 0; right: 0; bottom: 0;
    height: 100px;
    background: linear-gradient(180deg, var(--green) 0%, var(--green-dark) 100%);
    border-top: 4px solid var(--lime);
    display: flex;
    align-items: center;
    justify-content: center;
  }
  .website {
    color: var(--paper);
    font-size: 16px;
    opacity: .85;
    letter-spacing: .3px;
  }
</style>
</head>
<body>
<div class="canvas">
  <section class="card card-front">
    <div class="front-art" role="img" aria-label="Soft green background with large leaf shapes"></div>
    <div class="front-brand">Pacel Talent</div>
  </section>

  <section class="card card-back">
    <div class="back-brand">Pacel Talent</div>
    <div class="contact">
      <div class="contact-name">TOM WHITFORD</div>
      <div class="contact-role">Director</div>
      <div class="contact-line"><span class="label">M</span>0419 572 641</div>
      <div class="contact-line"><span class="label">E</span>tom@paceltalent.com.au</div>
      <div class="contact-address">Level 4, 238 Finch Terrace<br>Brisbane QLD 4000</div>
    </div>
    <div class="footer-band">
      <span class="website">www.paceltalent.com.au</span>
    </div>
  </section>
</div>
</body>
</html>
```